Hangover Drink Label Design- UK. Please read fully before submitting.

Sticky label design (55mm by 50 mm ) front and back for a small drink. Simple design which has to follow the basic layout of the pictures. PLEASE READ THE MOST HAVES AND MUST NOT HAVES CAREFULLY.

Would like to see different colour options and font- layout and words as given.

Target Market(s)

For people to drink before bed after a night out.

Colors

Designer to choose colors to be used in the design.

Requirements
Must have
• See the pictures MUST have all of these words. in " ".
• Front " Kelpmoorly" "Copper Lullaby" "Hangover Prevention"
• Back " Contains" then bullet points "Milk Thistle " Electrolytes" "Taurine" "Green Tea" "Ginseng" "Ginger" and "Kelpmoorly.com" with a barcode on the bottom.
Should not have
• Pictures/ photos of anything- animals fruit etc. No other words other than on the pictures ( see must haves)"

```html
<!DOCTYPE html>
<html lang="en">
<head>
<meta charset="UTF-8">
<title>Kelpmoorly – Copper Lullaby Label</title>
<link rel="stylesheet" href="https://fonts.googleapis.com/css2?family=Roboto:wght@300;500;700&family=Oswald:wght@700&display=swap">
<style>
  :root {
    --page-bg: #ffffff;
    --label-bg: #eef0f2;
    --label-edge: #d9dde1;
    --ink-dark: #1c1c1e;
    --ink-brand: #2a2a2c;
    --ribbon-red: #e8353f;
    --ribbon-magenta: #c2248f;
    --ribbon-purple: #6a3fd6;
    --ribbon-blue: #2f7fe8;
    --ribbon-cyan: #2ed3e6;
  }
  * { margin: 0; padding: 0; box-sizing: border-box; }
  html, body {
    width: 1200px;
    height: 1200px;
    overflow: hidden;
    background: var(--page-bg);
  }
  .canvas {
    width: 1200px;
    height: 1200px;
    display: flex;
    align-items: center;
    justify-content: center;
  }
  .label {
    position: relative;
    width: 640px;
    height: 700px;
    background: var(--label-bg);
    border: 2px solid var(--label-edge);
    border-radius: 6px;
    padding: 70px 50px 0 50px;
  }
  .brand-name {
    font-family: "Roboto", sans-serif;
    font-weight: 300;
    font-size: 76px;
    letter-spacing: 1px;
    color: var(--ink-brand);
    line-height: 1;
  }
  .product-name {
    margin-top: 48px;
    font-family: "Oswald", sans-serif;
    font-weight: 700;
    font-size: 84px;
    letter-spacing: 6px;
    line-height: 1.08;
    text-transform: uppercase;
    color: var(--ink-dark);
  }
  .ribbon-placeholder {
    margin: 22px 0 0 -12px;
    width: 540px;
    height: 100px;
    border-radius: 50px;
    background: linear-gradient(90deg,
      var(--ribbon-red) 0%,
      var(--ribbon-magenta) 30%,
      var(--ribbon-purple) 55%,
      var(--ribbon-blue) 80%,
      var(--ribbon-cyan) 100%);
    opacity: 0.85;
  }
  .tagline {
    margin: 24px 0 0 110px;
    width: 330px;
    font-family: "Roboto", sans-serif;
    font-weight: 500;
    text-transform: uppercase;
    color: var(--ink-dark);
    line-height: 1.15;
  }
  .tagline-top { font-size: 34px; letter-spacing: 0.5px; }
  .tagline-bottom { font-size: 30px; letter-spacing: 1px; }
  .tagline-rule {
    margin-top: 12px;
    height: 3px;
    background: var(--ink-dark);
    width: 330px;
  }
</style>
</head>
<body>
  <main class="canvas">
    <section class="label">
      <h1 class="brand-name">Kelpmoorly</h1>
      <h2 class="product-name">Copper<br>Lullaby</h2>
      <div class="ribbon-placeholder" role="img" aria-label="Decorative multicolour wavy ribbon running from red through purple to cyan"></div>
      <div class="tagline">
        <p class="tagline-top">Hangover</p>
        <p class="tagline-bottom">Prevention</p>
        <div class="tagline-rule"></div>
      </div>
    </section>
  </main>
</body>
</html>
```